Poster Design for Skeletal Wellness Alliance- Frame Strong Program

Skeletal Wellness Alliance is an non-profit health charity, developed the Frame Strong program.
Frame Strong is a workshop program which provides up-to-date training for healthcare professionals on the most appropriate, safe and effective way to prescribe exercise for

```html
<!DOCTYPE html>
<html lang="en">
<head>
<meta charset="utf-8">
<title>Frame Strong Workshops</title>
<link rel="stylesheet" href="https://fonts.googleapis.com/css2?family=Anton&family=Open+Sans:ital,wght@0,400;0,700;0,800;1,700&family=Roboto+Condensed:wght@700&display=swap">
<style>
  :root {
    --red: #c8102e;
    --ink: #111111;
    --grey-text: #5e5e5e;
    --caption-bg: rgba(20, 24, 34, 0.82);
    --white: #ffffff;
  }
  * { margin: 0; padding: 0; box-sizing: border-box; }
  html, body { width: 928px; height: 1200px; overflow: hidden; background: var(--white); }
  .poster { position: relative; width: 928px; height: 1200px; overflow: hidden; background: var(--white); font-family: "Open Sans", Arial, sans-serif; }
  .hero-photo {
    position: absolute; left: 280px; top: 60px; width: 640px; height: 400px;
    background: radial-gradient(ellipse at 55% 55%, #eddcd6 0%, #e6d2cc 40%, #f6f1ef 70%, rgba(255,255,255,0) 100%);
  }
  .backdrop { position: absolute; inset: 0; }
  .brand { position: absolute; left: 48px; top: 34px; }
  .brand-name { font-weight: 800; font-size: 56px; line-height: 1; color: var(--red); letter-spacing: -1px; }
  .brand-sub { margin-top: 8px; font-weight: 400; font-size: 22px; letter-spacing: 0.5px; color: var(--ink); }
  .headline {
    position: absolute; left: 48px; top: 176px;
    font-family: "Anton", Impact, sans-serif; font-size: 47px; line-height: 54px;
    color: var(--ink); text-transform: uppercase; letter-spacing: 0.3px;
  }
  .tagline {
    position: absolute; left: 48px; top: 494px; width: 860px;
    font-weight: 700; font-size: 26px; line-height: 34px; color: var(--white);
  }
  .features { position: absolute; left: 33px; top: 601px; display: flex; gap: 3px; }
  .feature {
    position: relative; width: 288px; height: 474px;
    background: linear-gradient(to bottom, #ffffff 0%, #ffffff 55%, #e4e4e4 100%);
    border: 2px solid #cfcfcf; border-radius: 6px; overflow: hidden;
    box-shadow: 0 2px 6px rgba(0,0,0,0.25);
  }
  .feature-photo { height: 150px; }
  .feature-photo.clinic { background: linear-gradient(160deg, #dfe6ee 0%, #c9d3de 60%, #a9b3c0 100%); }
  .feature-photo.training { background: linear-gradient(160deg, #8ea7c9 0%, #c96a5d 60%, #a83c36 100%); }
  .feature-photo.seminar { background: linear-gradient(160deg, #c9c2bb 0%, #8f8583 55%, #5e6d86 100%); }
  .feature-caption {
    height: 100px; padding: 8px 14px; background: var(--caption-bg);
    font-family: "Roboto Condensed", "Arial Narrow", sans-serif; font-weight: 700;
    font-size: 19px; line-height: 27px; color: var(--white);
  }
  .feature-text { padding: 14px 16px 0 16px; font-size: 17px; line-height: 22px; color: var(--grey-text); }
  .register {
    position: absolute; left: 0; right: 0; top: 1116px; text-align: center;
    font-weight: 700; font-style: italic; font-size: 17.5px; line-height: 27px; color: var(--ink);
  }
  .register .site { color: var(--red); }
</style>
</head>
<body>
<main class="poster">
  <div class="hero-photo" role="img" aria-label="Photo of four smiling seniors lifting red dumbbells"></div>

  <svg class="backdrop" width="928" height="1200" viewBox="0 0 928 1200" aria-hidden="true">
    <defs>
      <linearGradient id="red-band" x1="0" y1="0" x2="0" y2="1">
        <stop offset="0" stop-color="#d0103a"/>
        <stop offset="0.35" stop-color="#c8102e"/>
        <stop offset="1" stop-color="#8e0820"/>
      </linearGradient>
      <linearGradient id="grey-base" x1="0" y1="0" x2="0" y2="1">
        <stop offset="0" stop-color="#d6d6d6"/>
        <stop offset="1" stop-color="#a9a9a9"/>
      </linearGradient>
    </defs>
    <path d="M0 452 Q 464 396 928 392" fill="none" stroke="#9c9c9c" stroke-width="6"/>
    <path d="M0 460 Q 464 404 928 400 L928 1060 L0 1060 Z" fill="url(#red-band)"/>
    <path d="M0 1060 Q 464 1020 928 1060 L928 1200 L0 1200 Z" fill="url(#grey-base)"/>
  </svg>

  <header class="brand">
    <div class="brand-name">framestrong</div>
    <div class="brand-sub">FRAME STRONG WORKSHOPS</div>
  </header>

  <h1 class="headline">Do you work<br>with<br>osteoporosis<br>patients?</h1>

  <p class="tagline">If so we can help you bone up on the development of safe<br>exercise programs for fracture reduction.</p>

  <section class="features">
    <article class="feature">
      <div class="feature-photo clinic" role="img" aria-label="Photo of a smiling healthcare professional holding a clipboard"></div>
      <h2 class="feature-caption">Interactive practical<br>learning from expert<br>instructors</h2>
      <p class="feature-text">Learning from expert instructors to ensure mastery of exercises and concepts</p>
    </article>
    <article class="feature">
      <div class="feature-photo training" role="img" aria-label="Photo of a therapist guiding an older man through an arm exercise"></div>
      <h2 class="feature-caption">Learn the most recent<br>evidence-based<br>recommendations</h2>
      <p class="feature-text">For prescribing exercises aimed at reducing future fractures and bone loss as well as safely adapting exercise, Pilates and ADL’s.</p>
    </article>
    <article class="feature">
      <div class="feature-photo seminar" role="img" aria-label="Photo of professionals seated together in a workshop session"></div>
      <h2 class="feature-caption">Up-to-date information on<br>clinical practice guidelines<br>for osteoporosis</h2>
      <p class="feature-text">Integrated with current evidence-based information on prescribing exercise for the management of complex patients with co-morbidities</p>
    </article>
  </section>

  <p class="register">Register at <span class="site">framestrong.org</span> for upcoming workshops and receive access<br>to our pre-course materials and resources.</p>
</main>
</body>
</html>
```